Poster for List of Company Values

We need a poster to outline our Values which will be displayed in our office as well as posted on our website and other platforms (so need to allow for some flexibly in its application).

File attached outlines what we currently have with design and also our company style guide.

Note that we are looking for a modern, clean look, which still represents our core activities of construction and environmental services.

You can also reference our website here:

https://quorvelgroup.com.au/

Happy to answer any questions you might have.

Thanks for your interest,
Brent

Target Market(s)

Internal and External clients

Industry/Entity Type

Construction, water and recycling

Font styles to use
Sans Serif

Requirements
Must have
• All values on the one page. Graphic to represent each value. Also needs to use company logo
Nice to have
• Preference for poster to be orientated in landscape
Should not have
• Do not follow example provided, this is only to demonstrate what we have to date and also the text required

```html
<!DOCTYPE html>
<html lang="en">
<head>
<meta charset="utf-8">
<title>Quorvel Group – Our Values</title>
<link rel="stylesheet" href="https://fonts.googleapis.com/css2?family=Open+Sans:ital,wght@0,300;0,400;0,700;1,400&display=swap">
<style>
  :root {
    --paper: #f1f1f2;
    --paper-edge: #e4e4e6;
    --ink-grey: #555759;
    --deco-grey: #8a8a8a;
    --green-a: #00b050;
    --green-b: #00853b;
    --green-shade: #0a5e2c;
    --yellow-a: #ffc400;
    --yellow-b: #e9b33a;
    --yellow-shade: #8a6a12;
    --blue-a: #0070c8;
    --blue-b: #0c5fa8;
    --blue-shade: #0b3f74;
    --orange-a: #e06b30;
    --orange-b: #f0853c;
    --orange-shade: #9a3a10;
    --cyan-a: #1786c4;
    --cyan-b: #00b0ee;
    --cyan-shade: #0b4a86;
    --pink-a: #d93b86;
    --pink-b: #ff2d98;
    --pink-shade: #8e1553;
    --white: #ffffff;
  }
  * { box-sizing: border-box; margin: 0; padding: 0; }
  html, body { width: 947px; height: 1200px; overflow: hidden; }
  body {
    font-family: "Open Sans", Arial, sans-serif;
    background: linear-gradient(160deg, var(--paper) 0%, #fafafa 45%, var(--paper-edge) 100%);
    position: relative;
  }
  .value-card { position: absolute; color: var(--white); overflow: hidden; }
  .value-card .stripes { position: absolute; inset: 0; width: 100%; height: 100%; }
  .value-title {
    position: absolute;
    font-size: 53px;
    line-height: 0.88;
    letter-spacing: -1.5px;
    font-weight: 300;
    white-space: nowrap;
  }
  .value-title strong { font-weight: 700; display: block; }
  .value-title strong.inline { display: inline; }
  .value-marker { position: absolute; width: 100px; height: 88px; }
  .value-marker .icon { fill: none; stroke-width: 1.6; stroke-linecap: round; stroke-linejoin: round; }
  .value-text {
    position: absolute;
    font-style: italic;
    font-size: 15px;
    line-height: 1.0;
  }
  .loyal { left: 122px; top: 61px; width: 271px; height: 396px;
    background: linear-gradient(180deg, var(--green-a), var(--green-b)); }
  .initiative { left: 415px; top: 196px; width: 484px; height: 261px;
    background: linear-gradient(90deg, var(--yellow-a), var(--yellow-b)); }
  .team { left: 48px; top: 476px; width: 471px; height: 272px;
    background: linear-gradient(180deg, var(--blue-a), var(--blue-b)); }
  .respect { left: 542px; top: 476px; width: 311px; height: 244px;
    background: linear-gradient(90deg, var(--orange-a), var(--orange-b)); }
  .positive { left: 542px; top: 738px; width: 357px; height: 243px;
    background: linear-gradient(90deg, var(--cyan-a), var(--cyan-b)); }
  .honest { left: 122px; top: 769px; width: 397px; height: 369px;
    background: linear-gradient(180deg, var(--pink-a), var(--pink-b)); }

  .deco-squares { position: absolute; }
  .deco-squares rect { fill: var(--deco-grey); }

  .brand {
    position: absolute; left: 570px; top: 1036px;
    display: flex; align-items: center; gap: 50px;
    color: var(--ink-grey);
  }
  .brand-square { width: 70px; height: 70px; background: var(--ink-grey); }
  .brand-name { font-weight: 700; font-size: 33px; line-height: 0.95; letter-spacing: -0.5px; }
</style>
</head>
<body>

<svg class="deco-squares" style="left:419px;top:160px" width="66" height="66" viewBox="0 0 66 66" aria-hidden="true">
  <rect x="0" y="10" width="12" height="12"/><rect x="22" y="0" width="20" height="20"/>
  <rect x="50" y="12" width="8" height="8"/><rect x="50" y="26" width="8" height="8"/>
  <rect x="0" y="30" width="36" height="36"/><rect x="44" y="40" width="22" height="26"/>
</svg>
<svg class="deco-squares" style="left:868px;top:476px" width="44" height="46" viewBox="0 0 44 46" aria-hidden="true">
  <rect x="0" y="0" width="22" height="22"/><rect x="28" y="0" width="16" height="14"/>
  <rect x="0" y="28" width="8" height="8"/><rect x="12" y="28" width="14" height="14"/><rect x="30" y="28" width="6" height="6"/>
</svg>
<svg class="deco-squares" style="left:34px;top:770px" width="56" height="62" viewBox="0 0 56 62" aria-hidden="true">
  <rect x="0" y="0" width="18" height="18"/><rect x="27" y="0" width="29" height="32"/>
  <rect x="13" y="26" width="10" height="10"/><rect x="13" y="42" width="8" height="8"/>
  <rect x="26" y="42" width="16" height="18"/><rect x="46" y="40" width="10" height="10"/>
</svg>

<section class="value-card loyal">
  <svg class="stripes" viewBox="0 0 271 396" preserveAspectRatio="none" aria-hidden="true">
    <g stroke="#000" stroke-opacity="0.1" stroke-width="26" stroke-linecap="round">
      <line x1="130" y1="40" x2="170" y2="-20"/><line x1="160" y1="110" x2="260" y2="-20"/><line x1="230" y1="130" x2="300" y2="30"/>
    </g>
  </svg>
  <h2 class="value-title" style="left:27px;top:112px">be<strong>LOYAL</strong></h2>
  <svg class="value-marker" style="left:28px;top:226px" viewBox="0 0 100 88" role="img" aria-label="Handshake icon">
    <polygon points="6,3 100,3 53,88" fill="var(--green-shade)"/>
    <polygon points="0,0 92,0 46,82" fill="var(--white)"/>
    <g class="icon" stroke="var(--green-b)">
      <rect x="40" y="8" width="12" height="8" rx="1"/><path d="M43 8 v-2 h6 v2"/>
      <rect x="24" y="22" width="7" height="12" transform="rotate(-20 27 28)"/>
      <rect x="61" y="22" width="7" height="12" transform="rotate(20 64 28)"/>
      <path d="M31 25 l8 -3 l7 3 l7 -3 l8 3"/>
      <path d="M33 33 l6 6 q2 2 4 0 l8 -7"/><path d="M39 31 l5 5 M43 29 l5 5"/>
    </g>
  </svg>
  <p class="value-text" style="left:26px;bottom:34px;width:215px">We take care of our own and provide opportunities to listen and support each other.</p>
</section>

<section class="value-card initiative">
  <svg class="stripes" viewBox="0 0 484 261" preserveAspectRatio="none" aria-hidden="true">
    <g stroke="#000" stroke-opacity="0.09" stroke-width="26" stroke-linecap="round">
      <line x1="280" y1="40" x2="320" y2="-10"/><line x1="300" y1="110" x2="400" y2="-10"/><line x1="390" y1="140" x2="480" y2="10"/>
    </g>
  </svg>
  <h2 class="value-title" style="left:25px;top:18px">show<strong>INITIATIVE</strong></h2>
  <svg class="value-marker" style="left:28px;top:114px" viewBox="0 0 100 88" role="img" aria-label="Hand raising a flag icon">
    <polygon points="6,3 100,3 53,88" fill="var(--yellow-shade)"/>
    <polygon points="0,0 92,0 46,82" fill="var(--white)"/>
    <g class="icon" stroke="var(--yellow-shade)">
      <path d="M36 6 v26"/><path d="M36 7 l14 3 l-5 4 l5 4 l-14 -2"/>
      <path d="M30 28 h12 q3 0 3 3 v6 q0 3 -3 3 h-10 q-3 0 -3 -3 z"/>
      <path d="M30 32 h6 M30 36 h6"/>
      <rect x="45" y="27" width="7" height="13"/><rect x="52" y="25" width="6" height="17"/>
    </g>
  </svg>
  <p class="value-text" style="left:29px;bottom:24px;width:280px">We celebrate and recognize our own and encourage forward thinking.</p>
</section>

<section class="value-card team">
  <svg class="stripes" viewBox="0 0 471 272" preserveAspectRatio="none" aria-hidden="true">
    <g stroke="#000" stroke-opacity="0.1" stroke-width="26" stroke-linecap="round">
      <line x1="270" y1="50" x2="320" y2="-10"/><line x1="300" y1="110" x2="400" y2="-10"/><line x1="340" y1="170" x2="470" y2="0"/>
    </g>
  </svg>
  <h2 class="value-title" style="left:26px;top:22px">think<strong>TEAM</strong></h2>
  <svg class="value-marker" style="left:28px;top:126px" viewBox="0 0 100 88" role="img" aria-label="Joined hands icon">
    <polygon points="6,3 100,3 53,88" fill="var(--blue-shade)"/>
    <polygon points="0,0 92,0 46,82" fill="var(--white)"/>
    <g class="icon" stroke="var(--blue-shade)">
      <circle cx="46" cy="24" r="17" stroke-dasharray="1.5 2.5"/>
      <rect x="41" y="6" width="10" height="6"/>
      <path d="M40 12 h12 v12 h-12 z"/><path d="M40 16 h12 M40 20 h12"/>
      <path d="M28 36 l8 -8 l6 4 M64 36 l-8 -8 l-6 4"/>
      <path d="M26 34 l4 4 M66 34 l-4 4"/>
    </g>
  </svg>
  <p class="value-text" style="left:30px;bottom:28px;width:395px">We communicate effectively and work as a team by helping and supporting each other.</p>
</section>

<section class="value-card respect">
  <svg class="stripes" viewBox="0 0 311 244" preserveAspectRatio="none" aria-hidden="true">
    <g stroke="#000" stroke-opacity="0.1" stroke-width="26" stroke-linecap="round">
      <line x1="140" y1="40" x2="180" y2="-10"/><line x1="180" y1="100" x2="270" y2="-10"/><line x1="240" y1="140" x2="320" y2="30"/>
    </g>
  </svg>
  <h2 class="value-title" style="left:20px;top:16px">show<strong>RESPECT</strong></h2>
  <svg class="value-marker" style="left:24px;top:106px" viewBox="0 0 100 88" role="img" aria-label="Two thumbs up icon">
    <polygon points="6,3 100,3 53,88" fill="var(--orange-shade)"/>
    <polygon points="0,0 92,0 46,82" fill="var(--white)"/>
    <g class="icon" stroke="var(--orange-shade)">
      <rect x="24" y="14" width="5" height="12"/>
      <path d="M29 15 l4 -7 q2 -3 4 0 l-1 6 h6 q2 0 2 2 l-2 9 q-1 1 -2 1 h-11"/>
      <rect x="50" y="28" width="5" height="12"/>
      <path d="M55 29 l4 -7 q2 -3 4 0 l-1 6 h6 q2 0 2 2 l-2 9 q-1 1 -2 1 h-11"/>
    </g>
  </svg>
  <p class="value-text" style="left:22px;bottom:18px;width:270px">We value the diversity and opinions of all.</p>
</section>

<section class="value-card positive">
  <svg class="stripes" viewBox="0 0 357 243" preserveAspectRatio="none" aria-hidden="true">
    <g stroke="#000" stroke-opacity="0.08" stroke-width="26" stroke-linecap="round">
      <line x1="170" y1="30" x2="200" y2="-10"/><line x1="220" y1="80" x2="300" y2="-10"/><line x1="270" y1="140" x2="360" y2="20"/>
    </g>
  </svg>
  <h2 class="value-title" style="left:20px;top:28px">be<strong class="inline">POSITIVE</strong></h2>
  <svg class="value-marker" style="left:24px;top:92px" viewBox="0 0 100 88" role="img" aria-label="Positive mind icon">
    <polygon points="6,3 100,3 53,88" fill="var(--cyan-shade)"/>
    <polygon points="0,0 92,0 46,82" fill="var(--white)"/>
    <g class="icon" stroke="var(--cyan-shade)">
      <path d="M39 42 v-8 q-8 -4 -7 -13 q2 -12 14 -12 q12 0 13 11 l3 6 h-3 v5 q0 2 -2 2 h-4 v9"/>
      <circle cx="46" cy="20" r="6"/><path d="M46 17 v6 M43 20 h6"/>
      <path d="M46 10 v-2 M54 12 l1.5 -1.5 M38 12 l-1.5 -1.5 M56 20 h2 M36 20 h-2"/>
    </g>
  </svg>
  <p class="value-text" style="left:20px;bottom:22px;width:295px">SMILE : We are solutions focused and encourage a positive attitude turning a negative into a positive.</p>
</section>

<section class="value-card honest">
  <svg class="stripes" viewBox="0 0 397 369" preserveAspectRatio="none" aria-hidden="true">
    <g stroke="#000" stroke-opacity="0.1" stroke-width="26" stroke-linecap="round">
      <line x1="200" y1="40" x2="240" y2="-10"/><line x1="230" y1="130" x2="330" y2="-10"/><line x1="290" y1="190" x2="400" y2="40"/>
    </g>
  </svg>
  <h2 class="value-title" style="left:30px;top:96px">be <strong class="inline">OPEN</strong><br>and <strong class="inline">HONEST</strong></h2>
  <svg class="value-marker" style="left:28px;top:204px" viewBox="0 0 100 88" role="img" aria-label="Person holding a heart icon">
    <polygon points="6,3 100,3 53,88" fill="var(--pink-shade)"/>
    <polygon points="0,0 92,0 46,82" fill="var(--white)"/>
    <g class="icon" stroke="var(--pink-shade)">
      <circle cx="46" cy="12" r="6"/>
      <path d="M33 40 v-10 q0 -10 13 -10 q13 0 13 10 v10"/>
      <path d="M46 36 l-5 -5 q-2 -3 1 -5 q3 -1 4 2 q1 -3 4 -2 q3 2 1 5 z"/>
      <path d="M33 30 l7 8 h12 l7 -8"/>
    </g>
  </svg>
  <p class="value-text" style="left:30px;bottom:26px;width:330px">We are clear and open with each other, and provide an approachable and friendly environment.</p>
</section>

<div class="brand">
  <span class="brand-square" aria-hidden="true"></span>
  <span class="brand-name">QUORVEL<br>Group</span>
</div>

</body>
</html>
```